Advertising Portal Needs eBrochure

Hi Crowders! Our advertising portal, which focus on the new launches property, needs an online brochure to promote to potential advertisers the benefits of advertising their projects with us. These advertisers will be mainly real estate developers and agencies.

WHAT WE LOOKING FOR
We do not want over-fanciful designs that makes the content hard to read. The use of illustrations and graphics/symbols related to covered topics are encouraged. The overall design should portrait our advertising efficiency through online and social media means. Our website - www.brightkeyhomes.sg.

For draft purposes, just do up the front page, back page, and few inner pages, preferably to include one illustration chart (either on page 7/8). Size wise probably A5 portrait or landscape, for future printing into a booklet.

WORK COMPLETION AND PAYMENT
The $500 stated here is 50% of the payment. Upon getting a desired draft design, we will need you to work on the full content with slight amendments along the way. Once done, we will be paying the balance $500, and we will need the pdf file as well as the work file.

Let your design juice flow, and hope we can work with you!
Updates

Hi Crowders! Thank you for your submissions. We are closing the project as we've decided on a design. It's a pity we can only select one design, as there are a number of good works. Hope we will have a chance to work together on our upcoming projects. Cheers =)

Target Market(s)

Real estate developers, real estate agencies, and perhaps to an extent, individual property sales agent.

Industry/Entity Type

Advertising

Requirements
Should not have
• We prefer not to have much real people kind of stock images. Try not to use images from our portal as we do not have the ownerships. Instead, you can use stock images of property developments artist impression that gives a similar feel.

```html
<!DOCTYPE html>
<html lang="en">
<head>
<meta charset="utf-8">
<title>BrightKey Homes eBrochure</title>
<link href="https://fonts.googleapis.com/css2?family=Arimo:wght@400;700&family=Ubuntu:wght@500;700&family=Tinos:ital,wght@0,400;0,700;1,400&display=swap" rel="stylesheet">
<style>
:root{
  --bg:#e9ebe6;
  --paper:#f7f7f5;
  --panel:#dcdcdc;
  --green:#8dc63f;
  --green-dark:#6fa82a;
  --red:#e2585e;
  --yellow:#e8b923;
  --teal:#3fb3ad;
  --ink:#333333;
  --ink-soft:#555555;
}
*{margin:0;padding:0;box-sizing:border-box}
html,body{width:1200px;height:800px;overflow:hidden;background:var(--bg)}
body{position:relative;font-family:"Arimo",Arial,sans-serif;color:var(--ink)}
.abs{position:absolute}

/* back cover */
.back-cover{left:538px;top:95px;width:362px;height:247px;background:var(--paper);box-shadow:0 3px 8px rgba(0,0,0,.25)}
.cover-photo{left:0;top:0;width:254px;height:247px;background:linear-gradient(180deg,#6d6a8c 0%,#9a8fa6 30%,#8c93a8 55%,#3d4a3a 80%,#243223 100%)}
.cover-strip{left:254px;top:0;width:4px;height:247px;background:var(--green)}
.cover-panel{left:258px;top:0;width:104px;height:247px;background:var(--panel);padding:8px 8px}
.brand{display:flex;align-items:center;gap:4px;font-family:"Ubuntu",sans-serif;font-weight:700;color:var(--green);font-size:9px;white-space:nowrap}
.brand-mark{flex:none;width:8px;height:8px;border-radius:50%;background:var(--green)}
.contact-list{list-style:none;margin-top:14px}
.contact-list li{display:flex;gap:5px;font-size:5.6px;font-weight:700;color:var(--ink);line-height:1.35;margin-bottom:9px}
.contact-icon{flex:none;width:6px;height:6px;background:var(--green);margin-top:1px}

/* spread */
.spread{left:262px;top:425px;width:716px;height:264px;box-shadow:0 3px 8px rgba(0,0,0,.25)}
.page{top:0;width:358px;height:264px;background:var(--paper);overflow:hidden}
.page-left{left:0}
.page-right{left:358px;border-left:1px solid #cfcfcf}
.page-rule{left:6px;top:4px;width:4px;height:256px;background:var(--green)}
.page-right .page-rule{left:auto;right:6px}
h2.section{font-family:"Ubuntu",sans-serif;font-weight:700;color:var(--green);font-size:9.5px;white-space:nowrap}
h3.sub{font-family:"Ubuntu",sans-serif;font-weight:700;color:var(--green);font-size:10px;white-space:nowrap}
p.body{font-size:6.2px;line-height:1.45;color:var(--ink-soft);text-indent:8px}
.ribbon{left:38px;width:84px;height:20px;color:#fff;font-family:"Tinos",serif;font-style:italic;font-size:4.8px;line-height:1.25;padding:3px 4px 0 20px;clip-path:polygon(0 0,100% 0,94% 50%,100% 100%,0 100%)}
.ribbon svg{position:absolute;left:5px;top:6px}
.r-red{background:var(--red)}.r-yellow{background:var(--yellow)}.r-teal{background:var(--teal)}
.rank{font-family:"Ubuntu",sans-serif;font-weight:700;font-size:11px;color:var(--ink)}
.rank-name{font-family:"Tinos",serif;font-size:5px;color:var(--ink);white-space:nowrap}
.project-box{background:var(--green);color:#fff;font-family:"Tinos",serif;font-weight:700;display:flex;align-items:center;justify-content:center;gap:6px}
.footer-brand{left:288px;top:246px}
.footer-brand .brand{font-size:7px}
.footer-brand .brand-mark{width:7px;height:7px}
.step-num{left:6px;top:12px;width:12px;height:12px;border-radius:50%;background:var(--ink);color:#fff;font-size:7px;font-weight:700;display:flex;align-items:center;justify-content:center}
.source{height:22px;color:#fff;font-family:"Tinos",serif;font-size:5.5px;display:flex;align-items:center;justify-content:center;text-align:center;line-height:1.1}
.flow-caption{font-family:"Tinos",serif;font-weight:700;font-size:5.5px;color:var(--ink);text-align:center}
.band{color:var(--ink);font-family:"Tinos",serif;font-weight:700;display:flex;align-items:center;justify-content:center;white-space:nowrap}
</style>
</head>
<body>

<section class="back-cover abs" aria-label="Back cover">
  <div class="cover-photo abs" role="img" aria-label="Artist impression of a modern residential condominium at dusk with pool and palm trees"></div>
  <div class="cover-strip abs"></div>
  <div class="cover-panel abs">
    <div class="brand"><span class="brand-mark"></span>BrightKey Homes</div>
    <ul class="contact-list">
      <li><span class="contact-icon"></span>42 Larkfield Road #05-11, Westgate Park, Singapore 560218</li>
      <li><span class="contact-icon"></span>+(65) 90418827</li>
      <li><span class="contact-icon"></span>+(65) 63125490</li>
      <li><span class="contact-icon"></span>hello@brightkeyhomes.sg</li>
      <li><span class="contact-icon"></span>www.brightkeyhomes.sg</li>
    </ul>
  </div>
</section>

<section class="spread abs" aria-label="Inner spread">
  <article class="page page-left abs">
    <div class="page-rule abs"></div>
    <h2 class="section abs" style="left:22px;top:10px">EMAIL BLASTING</h2>
    <div class="abs" style="left:22px;top:25px;width:318px">
      <p class="body">Want immediate attention for a new launch project? A promotion? A Re-launch? Or project coming to completion? Consumers are always interested with such events. Let us help you to spread this to public by notifying our subscribers as well as local agents, on such important updates through our emails blasting service.</p>
      <p class="body" style="margin-top:3px">How is it different from sending your own? Well, beside avoiding the hassle - a trusted name, recognized server, and a well-designed newsletter - will better catch the recipients attention, less likely to end in spam, and our targeted recipients are consumers with genuine interest and our subscribers numbers are growing fast.</p>
    </div>
    <h3 class="sub abs" style="left:26px;top:117px">How Our Marketing Campaigns Boost Your Project Awareness</h3>

    <div class="ribbon r-red abs" style="top:137px"><svg width="8" height="8" viewBox="0 0 8 8"><circle cx="4" cy="2.5" r="2" fill="#fff"/><path d="M0 8a4 3 0 0 1 8 0z" fill="#fff"/></svg>Tens of thousands of genuine property searchers monthly</div>
    <span class="rank abs" style="left:124px;top:143px">01</span>
    <span class="rank-name abs" style="left:126px;top:158px">SearchHub</span>

    <div class="ribbon r-yellow abs" style="top:169px"><svg width="8" height="8" viewBox="0 0 8 8"><path d="M4 0a3 3 0 0 1 2 5v1H2V5A3 3 0 0 1 4 0z" fill="#fff"/><rect x="2.5" y="6.5" width="3" height="1.3" fill="#fff"/></svg>Reach to tens of thousands of property consumers</div>
    <span class="rank abs" style="left:124px;top:175px">02</span>
    <span class="rank-name abs" style="left:124px;top:190px">SocialSpace</span>

    <div class="ribbon r-teal abs" style="top:201px"><svg width="8" height="8" viewBox="0 0 8 8"><rect x="0" y="4" width="2" height="4" fill="#fff"/><rect x="3" y="2" width="2" height="6" fill="#fff"/><rect x="6" y="0" width="2" height="8" fill="#fff"/></svg>Hundreds of thousands of eyeballs</div>
    <span class="rank abs" style="left:124px;top:207px">03</span>
    <span class="rank-name abs" style="left:118px;top:222px">Lionport Courier</span>

    <svg class="abs" style="left:164px;top:170px" width="58" height="30" viewBox="0 0 58 30" aria-hidden="true">
      <g stroke="var(--green)" stroke-width="3" fill="none">
        <path d="M2 9h36M2 15h36M2 21h36"/>
      </g>
      <path d="M36 2l20 13-20 13z" fill="var(--green)"/>
    </svg>
    <div class="project-box abs" style="left:225px;top:161px;width:98px;height:54px;font-size:9px">
      <span>Your<br>Project</span>
      <svg width="26" height="24" viewBox="0 0 26 24" aria-hidden="true"><path d="M13 1L1 12h4v11h16V12h4z" fill="#fff"/><rect x="8" y="14" width="4" height="4" fill="var(--green)"/><rect x="14" y="14" width="4" height="4" fill="var(--green)"/></svg>
    </div>
    <div class="footer-brand abs"><div class="brand"><span class="brand-mark"></span>BrightKey Homes</div></div>
  </article>

  <article class="page page-right abs">
    <div class="page-rule abs"></div>
    <div class="step-num abs">3</div>
    <h2 class="section abs" style="left:22px;top:11px;font-size:10px">Your Project Gains Huge Awareness From BrightKeyHomes.sg</h2>
    <p class="body abs" style="left:16px;top:28px;width:322px">Even when your project isn't actively marketing, it will still receive great interest and awareness from quality consumers, and here is how.</p>
    <h2 class="section abs" style="left:16px;top:55px">CROSS TRAFFIC</h2>
    <p class="body abs" style="left:16px;top:70px;width:322px">The marketing campaigns on the many other projects will generates high number of visitors to our portal, and these visitors has a high chance to see your project as well.</p>
    <h3 class="sub abs" style="left:24px;top:93px;font-size:8px">How Your Project Gains Constant Awareness From BrightKeyHomes.sg</h3>

    <div class="source abs" style="left:24px;top:115px;width:48px;background:var(--red)">SearchHub</div>
    <div class="source abs" style="left:102px;top:115px;width:52px;background:var(--yellow)">SocialSpace</div>
    <div class="source abs" style="left:181px;top:115px;width:53px;background:var(--teal)">Lionport<br>Courier</div>

    <svg class="abs" style="left:24px;top:140px" width="212" height="18" viewBox="0 0 212 18" aria-hidden="true">
      <g fill="var(--green)"><path d="M21 0h6v9h4l-7 8-7-8h4z"/><path d="M101 0h6v9h4l-7 8-7-8h4z"/><path d="M180 0h6v9h4l-7 8-7-8h4z"/></g>
    </svg>
    <div class="flow-caption abs" style="left:24px;top:160px;width:212px">Marketing activities for many other projects in BrightKey Homes</div>
    <div class="band abs" style="left:24px;top:171px;width:212px;height:25px;background:var(--green);font-size:5.5px">Project 1 - Project 2 - Project 3 - Project 4 - Project 5 - Project 6</div>
    <svg class="abs" style="left:24px;top:199px" width="212" height="14" viewBox="0 0 212 14" aria-hidden="true">
      <g fill="var(--red)"><path d="M41 0h3v8h3l-4.5 5-4.5-5h3z"/><path d="M103 0h3v8h3l-4.5 5-4.5-5h3z"/><path d="M165 0h3v8h3l-4.5 5-4.5-5h3z"/></g>
    </svg>
    <div class="flow-caption abs" style="left:24px;top:216px;width:212px">Huge Traffics Flows To</div>
    <div class="band abs" style="left:24px;top:226px;width:213px;height:22px;background:var(--teal);font-size:8px">BrightKeyHomes</div>
    <svg class="abs" style="left:243px;top:228px" width="28" height="18" viewBox="0 0 28 18" aria-hidden="true">
      <g stroke="var(--green)" stroke-width="2" fill="none"><path d="M0 5h18M0 9h18M0 13h18"/></g>
      <path d="M17 1l10 8-10 8z" fill="var(--green)"/>
    </svg>
    <div class="project-box abs" style="left:273px;top:214px;width:66px;height:36px;font-size:7px;gap:4px">
      <span>Your<br>Project</span>
      <svg width="18" height="16" viewBox="0 0 26 24" aria-hidden="true"><path d="M13 1L1 12h4v11h16V12h4z" fill="#fff"/><rect x="8" y="14" width="4" height="4" fill="var(--green)"/><rect x="14" y="14" width="4" height="4" fill="var(--green)"/></svg>
    </div>
  </article>
</section>

</body>
</html>
```